We have 'joined together' 6 micro-sites with a common theme. Looking to upgrade the design of a total of 26 pages on the abovementioned sites, whilst maintaining a common look and feel.

Goal is to improve customer experience and conversion rate, whilst maintaining Vantro rankings. New design to be responsive to different devices and SEO optimised

We prefer simple designs with the cleaness of Zelqo.com, however with more descriptive text. Target audience are business managers and owners, so site should convey professional capability, with a hint of playfulness. After all data can be fun? No?

See attached doc for further details.

Update: 19/8/2014. Following further consideration, the HTML coding no longer required. Once design is finalised, we require a PSD file for each page showing the full page layout, including all images and icons. We will extract the relevant bits from the PSD and do the coding and css inhouse.
Updates

Hi All The Pelquin Collective - PSD Design Only. HTML no longer required Following further consideration, the HTML / Css coding aspect of the project NO longer required. Once design is finalised, we require a PSD file from you for each of the 26 web pages, showing the page layout and including all images and icons. If one page layout is the same as another, then we request that you just supply images and icons for that page in a PSD file. We will then extract the relevant bits from the PSD and we will do the coding and css inhouse. Our main aim is to get an awesome, blow-your-sox-off design that compels users to convert. Many thanks in anticipation Oliver.

Project Deadline Extended
Reason: Changed deliverables from PSD, HTML and Coding t o PSD only. Hopefully this change will allow previous designers who were not interested to reconsider. Many thanks Oliver

Target Market(s)

Target market is business & IT managers within Australian organisations who are having problems with their data. Site must convey the impression that we are:
1) Very capable
2) Professional in our dealings
3) Reliable & trustworthy
4) Just a little bit quirky

Aprox. 60% of users are female, 40% male. Typically in the 30 to 55 year old bracket.

Number 1 requirements is that we don't embarrass our clients in any way.
2nd is that we do a good high quality job, delivering a good result.

We are not the cheapest nor the most expensive data shop around. We offer good value-for-money solutions. We are also reliable, friendly and available

Industry/Entity Type

Business

Font styles to use
Sans Serif

Requirements
Must have
• Simple yet information dense design. The "who we are" and "what we do" to be immediately visible above the fold. Images to be high quality. Good usability.
Simple navigation structure. Easy for users to find the info that they want.

In summary a simple, but good looking site, that compels users to contact us
Should not have
• No flash, fancy automation, rotating images, pop-ups etc.

```html
<!DOCTYPE html>
<html lang="en">
<head>
<meta charset="utf-8">
<title>The Pelquin Collective</title>
<link rel="stylesheet" href="https://fonts.googleapis.com/css2?family=Nunito+Sans:wght@400;600;700;800&family=Open+Sans:wght@400;600;700&display=swap">
<style>
:root{
  --page-bg:#c9d0d1;
  --white:#ffffff;
  --ink:#1c1c1c;
  --body-text:#6f6f6f;
  --brand-blue:#0a56a8;
  --cyan:#1aa8e6;
  --orange:#f39a1e;
  --footer-bg:#1d2430;
  --footer-text:#d9dde2;
  --quote-grey:#d6d6d6;
  --hero-a:#dfe8ef;
  --hero-b:#7d93a8;
  --hero-c:#2a3d57;
}
*{box-sizing:border-box;margin:0;padding:0}
html,body{width:1200px;height:2194px;overflow:hidden}
body{background:var(--page-bg);font-family:"Open Sans",Arial,sans-serif;color:var(--ink)}
.page{position:absolute;left:98px;top:0;width:1012px;height:2194px;background:var(--white)}
section,header,footer{position:relative;width:1012px}

/* header */
.site-header{height:44px}
.brand{position:absolute;left:23px;top:11px;display:flex;align-items:center;gap:8px;font-family:"Nunito Sans",sans-serif;font-weight:800;font-size:19px;color:var(--ink)}
.brand-mark{width:12px;height:12px;background:var(--cyan)}
.main-nav{position:absolute;right:26px;top:13px;display:flex;gap:30px;font-family:"Nunito Sans",sans-serif;font-weight:700;font-size:13px}
.main-nav a{color:var(--ink);text-decoration:none;padding-bottom:5px}
.main-nav a.current{border-bottom:2px solid var(--orange)}

/* hero */
.hero{height:322px;background:linear-gradient(100deg,var(--hero-a) 0%,var(--hero-b) 45%,var(--hero-c) 100%)}
.hero-tagline{position:absolute;left:165px;top:138px;width:676px;height:53px;background:var(--cyan);color:var(--white);font-family:"Nunito Sans",sans-serif;font-weight:700;font-size:25px;line-height:53px;text-align:center}

/* intro */
.intro{height:463px}
.intro-col{position:absolute;top:29px;text-align:center}
.intro-col.who{left:121px;width:320px}
.intro-col.what{left:538px;width:364px}
.intro-icon{display:block;margin:0 auto;height:56px}
.intro-col h2{font-family:"Nunito Sans",sans-serif;font-weight:800;font-size:25px;margin-top:20px;margin-bottom:12px;letter-spacing:-.3px}
.intro-col p{font-size:11px;line-height:16px;color:var(--body-text);margin-bottom:16px}

/* testimonials */
.testimonials{height:678px;background:var(--brand-blue)}
.testimonials h2{position:absolute;top:39px;width:100%;text-align:center;color:var(--white);font-family:"Nunito Sans",sans-serif;font-weight:800;font-size:27px}
.quote-card{position:absolute;width:425px;background:var(--white);text-align:center;padding:0 40px;display:flex;flex-direction:column;align-items:center}
.quote-card .avatar{width:34px;height:34px;margin-top:17px;margin-bottom:10px;background:linear-gradient(135deg,#c9a58b,#6b4c3b)}
.quote-card .avatar.dark{background:linear-gradient(135deg,#2b2b2b,#0a0a0a)}
.quote-card .quote-mark{position:absolute;right:28px;top:12px;font-family:Georgia,serif;font-size:44px;line-height:44px;color:var(--quote-grey)}
.quote-card p{font-size:14.5px;line-height:19px;color:var(--ink)}
.card-l1{left:69px;top:110px;height:138px}
.card-l2{left:69px;top:272px;height:139px}
.card-l3{left:69px;top:435px;height:180px}
.card-r1{left:519px;top:110px;height:182px}
.card-r2{left:519px;top:314px;height:116px}
.card-r3{left:519px;top:454px;height:121px}

/* partners */
.partners{height:193px}
.partners h3{position:absolute;top:28px;width:100%;text-align:center;color:var(--orange);font-family:"Nunito Sans",sans-serif;font-weight:700;font-size:14px}
.partner-badge{position:absolute;top:62px;height:87px}
.badge-1{left:130px;width:88px}
.badge-2{left:297px;width:88px}
.badge-3{left:456px;width:98px}
.badge-4{left:626px;width:100px}
.badge-5{left:795px;width:92px}

/* footer */
.site-footer{height:301px;background:var(--footer-bg);color:var(--footer-text)}
.footer-col{position:absolute;top:47px}
.footer-col h4{font-family:"Nunito Sans",sans-serif;font-weight:700;font-size:15px;color:var(--white);margin-bottom:12px}
.footer-col p,.footer-col li{font-size:11.5px;line-height:23px;list-style:none}
.about{left:73px;width:255px}
.about strong{color:var(--white)}
.about .phone{color:var(--cyan);font-weight:700}
.company{left:372px}
.company li.current{color:var(--orange)}
.services{left:516px;top:80px}
.newsletter{left:668px;width:280px}
.signup{display:flex;margin-top:10px}
.signup .field{width:206px;height:26px;background:var(--white);color:#9a9a9a;font-size:10px;line-height:26px;padding-left:8px}
.signup .submit{width:70px;height:26px;background:var(--orange);color:var(--white);font-size:11px;font-weight:700;line-height:26px;text-align:center}
.social{position:absolute;left:193px;top:85px;display:flex;gap:6px}
.social span{width:22px;height:22px;background:#6f7886}
.footer-brand{position:absolute;left:168px;top:140px;display:flex;align-items:center;gap:6px;font-family:"Nunito Sans",sans-serif;font-weight:800;font-size:13px;color:#4c5563;white-space:nowrap}
.footer-brand .dot{width:9px;height:9px;background:#4c5563}

/* bottom links */
.bottom-links{height:193px;text-align:center}
.bottom-links nav{position:absolute;top:20px;width:100%;font-size:12.5px;line-height:22px;font-weight:600;color:var(--ink)}
.copyright{position:absolute;top:130px;width:100%;font-size:12.5px;font-weight:700}
.copyright span{color:var(--cyan)}
</style>
</head>
<body>
<div class="page">

  <header class="site-header">
    <div class="brand"><span class="brand-mark"></span>The Pelquin Collective</div>
    <nav class="main-nav">
      <a class="current">Home</a><a>Blog</a><a>Contact</a><a>Policy</a><a>Disclaimer</a><a>Privacy</a>
    </nav>
  </header>

  <section class="hero" role="img" aria-label="Photograph of two business colleagues in suits reviewing work together">
    <div class="hero-tagline">Helping you creatively generate real value from your data</div>
  </section>

  <section class="intro">
    <div class="intro-col who">
      <svg class="intro-icon" viewBox="0 0 56 56" width="56" height="56" fill="none" stroke="#1c1c1c" stroke-width="3">
        <circle cx="28" cy="18" r="10"/>
        <path d="M8 50 C10 36 18 32 28 32 C38 32 46 36 48 50 Z"/>
      </svg>
      <h2>Who we are.</h2>
      <p>The Pelquin Collective is a Melbourne based business offering a comprehensive<br>range of data services. We specialise in data analysis, data cleansing,<br>data mining, data scraping and data warehouses.</p>
      <p>Our goal is to help you extract value from your data in the form of pragmatic insights, trends and relationships. And then to analyse, interpret and use these findings in innovative ways that empower you to manage your organisation for greater profit, with improved decision-making and enhanced strategic, tactical and operational insight.</p>
      <p>Reap the rewards from a data project. Click on the following to see how<br>we can help you with your:</p>
    </div>
    <div class="intro-col what">
      <svg class="intro-icon" viewBox="0 0 56 56" width="56" height="56" fill="#1c1c1c">
        <rect x="10" y="38" width="6" height="14"/>
        <rect x="20" y="30" width="6" height="22"/>
        <rect x="30" y="24" width="6" height="28"/>
        <rect x="40" y="16" width="6" height="36"/>
        <path d="M8 28 L30 10" stroke="#1c1c1c" stroke-width="3"/>
        <path d="M24 7 L34 6 L32 15 Z"/>
      </svg>
      <h2>What we do.</h2>
      <p>Our core speciality is solving business problems that require complex data analysis, cleansing, mining or modelling techniques.<br>Your benefits include:</p>
      <p>Fast ROI: Quick access to skilled data professionals, without the overhead of building and maintaining your own infrastructure and team. Our fees are typically small in contrast to the additional profits or savings that our projects generate for our clients.</p>
      <p>Innovative practical solutions: We find smart ways to extract useful information from incomplete and disorganised data. We also have extensive industry experience AND the quantitative rigour to generate innovative yet pragmatic value-adding solutions.</p>
      <p>Connected to major universities. We have relationships.</p>
    </div>
  </section>

  <section class="testimonials">
    <h2>Testimonials.</h2>
    <div class="quote-card card-l1"><span class="quote-mark">&ldquo;&rdquo;</span><div class="avatar" role="img" aria-label="Client portrait"></div><p>i got my license in only 3 weeks! I would like to thank Marek!</p></div>
    <div class="quote-card card-l2"><span class="quote-mark">&ldquo;&rdquo;</span><div class="avatar dark" role="img" aria-label="Client portrait"></div><p>There are many variations of passages<br>Lorem Ipsum available, majority have suffered.</p></div>
    <div class="quote-card card-l3"><span class="quote-mark">&ldquo;&rdquo;</span><div class="avatar" role="img" aria-label="Client portrait"></div><p>Lorem Ipsum which looks reasonable.<br>The generated Lorem Ipsum is therefore always free from repetition, injected humour, or non-characteristic words etc.</p></div>
    <div class="quote-card card-r1"><span class="quote-mark">&ldquo;&rdquo;</span><div class="avatar" role="img" aria-label="Client portrait"></div><p>Contrary to popular belief, Lorem Ipsum is not simply random text. It has roots in a piece of classical Latin literature from 45 BC, making it over 2000 years old.</p></div>
    <div class="quote-card card-r2"><span class="quote-mark">&ldquo;&rdquo;</span><div class="avatar" role="img" aria-label="Client portrait"></div><p>My mother and i went here, love them!</p></div>
    <div class="quote-card card-r3"><span class="quote-mark">&ldquo;&rdquo;</span><div class="avatar" role="img" aria-label="Client portrait"></div><p>Did my lessons at Velmora Driving and got my license.</p></div>
  </section>

  <section class="partners">
    <h3>Some people we work with.</h3>
    <svg class="partner-badge badge-1" viewBox="0 0 88 87" role="img" aria-label="Partner certification badge"><circle cx="44" cy="38" r="32" fill="#1c1c1c"/><rect x="18" y="76" width="52" height="8" fill="#1c1c1c"/></svg>
    <svg class="partner-badge badge-2" viewBox="0 0 88 87" role="img" aria-label="Partner certification badge"><circle cx="44" cy="38" r="32" fill="none" stroke="#1c1c1c" stroke-width="6"/><rect x="18" y="76" width="52" height="8" fill="#1c1c1c"/></svg>
    <svg class="partner-badge badge-3" viewBox="0 0 98 87" role="img" aria-label="Partner listing badge"><rect x="4" y="14" width="90" height="58" fill="#1c1c1c"/></svg>
    <svg class="partner-badge badge-4" viewBox="0 0 100 87" role="img" aria-label="Quality standard badge"><rect x="6" y="16" width="88" height="48" fill="none" stroke="#1c1c1c" stroke-width="5"/><rect x="14" y="70" width="72" height="6" fill="#1c1c1c"/></svg>
    <svg class="partner-badge badge-5" viewBox="0 0 92 87" role="img" aria-label="Association seal"><circle cx="46" cy="43" r="36" fill="#8a8a8a"/><circle cx="46" cy="43" r="26" fill="none" stroke="#ffffff" stroke-width="2"/></svg>
  </section>

  <footer class="site-footer">
    <div class="footer-col about">
      <h4>About us</h4>
      <p>If you have data and a question, challenge or opportunity, we can help. We've been around since 2005 and worked on a diverse range of projects. <strong>Call us</strong> for a friendly discussion on <span class="phone">1300 555 014</span> or submit the contact us form.</p>
    </div>
    <div class="footer-col company">
      <h4>Company</h4>
      <ul><li>Home</li><li class="current">Blog</li><li>Contact</li><li>Policy</li><li>Disclaimer</li><li>Privacy</li></ul>
    </div>
    <div class="footer-col services">
      <ul><li>Data Analysis</li><li>Data cleansing</li><li>Data mining</li><li>Data scraping</li><li>Data warehouse</li><li>Data resources</li></ul>
    </div>
    <div class="footer-col newsletter">
      <h4>Newsletter</h4>
      <div class="signup"><div class="field">Email address</div><div class="submit">Submit</div></div>
      <div class="social"><span></span><span></span><span></span></div>
      <div class="footer-brand"><span class="dot"></span>The Pelquin Collective</div>
    </div>
  </footer>

  <section class="bottom-links">
    <nav>
      Blog | Comments Policy | Contact Us | Disclaimer | Home | Privacy Statement | Log in<br>
      Algorithm Creation | Cleansing Nimbra CRM Data | Customer Analysis | Data Analysis | Data Analysis Methods | Data Checking | Data Cleansing<br>
      Data Deduplication | Data Management | Data Merging | Data Migration | Data Mining | Data Scraping | Data Verification | Data Warehouse<br>
      Data Warehouse Methodology | Financial Analysis | Procurement Analysis | QRVX Report Writing | Text Analysis
    </nav>
    <p class="copyright">&copy; 2014 by <span>The Pelquin Collective</span>, Inc.</p>
  </section>

</div>
</body>
</html>
```